Mireva Party Planning Brochure

I am beginning a new Party Planning business and need a brochure outlining my services. We are offering a full range of party/event-related planning services. These include Catering Halls/Restaurants, Photography/Video, International DJ's and Bands, Flowers, Tuxedos/Gowns, Limousines and Specialized Entertainers such as Clowns and Face Painters, Middle Eastern Belly Dancers, and Musical Impersonators (specifically, Dell Maronett impersonator). I would like a festive design, showing people having a good time in a festive setting. No vulgar or inappropriate photos or language, please.

Target Market(s)

Primarily, newly engaged couples. As for ethnic preference, Greek-speaking clientele.

Future brides, new parents and newly engaged couples, primarily in the Greek market.

Industry/Entity Type

Business

Font styles to use
Sans Serif

Colors
33a6d7

Requirements
Must have
• Mention of speaking Greek and Spanish. Festive design. I need to have this phrase included exactly as you see it
• I need the brochure to look, read and exude "happy".
Nice to have
• Pictures of party atmosphere. A lively room.
Should not have
• No vulgarities, no inappropriate pictures. No drunken photos or offensive images.

```html
<!DOCTYPE html>
<html lang="en">
<head>
<meta charset="utf-8">
<title>Mireva Party Planning – Flyer</title>
<link rel="stylesheet" href="https://fonts.googleapis.com/css2?family=Crimson+Pro:wght@600;700&family=Fira+Sans:wght@400;500;600&display=swap">
<style>
  :root {
    --brand-blue: #33a6d7;
    --ink: #1e1e1e;
    --paper: #ffffff;
    --backdrop: #3a2a22;
    --photo-party-a: #5a3a2c;
    --photo-party-b: #c9a089;
    --photo-food-a: #e9e1d2;
    --photo-food-b: #9fae6a;
  }
  * { margin: 0; padding: 0; box-sizing: border-box; }
  html, body { width: 1200px; height: 1000px; overflow: hidden; }
  body {
    background: var(--backdrop);
    position: relative;
    font-family: "Fira Sans", Arial, sans-serif;
  }
  .card {
    position: absolute;
    top: 119px;
    width: 508px;
    height: 762px;
    overflow: hidden;
  }
  .card--front { left: 68px; background: var(--brand-blue); }
  .card--back { left: 639px; background: var(--paper); }
  .card__shapes { position: absolute; inset: 0; }

  .front__title {
    position: absolute; top: 38px; left: 0; right: 0;
    text-align: center;
    font-family: "Crimson Pro", Georgia, serif;
    font-weight: 700; font-size: 32px;
    color: var(--paper);
  }
  .front__footer {
    position: absolute; top: 642px; left: 0; right: 0;
    text-align: center;
    color: var(--paper);
    font-size: 19px; line-height: 24px;
  }
  .front__footer strong, .front__url { font-weight: 600; }

  .back__title {
    position: absolute; top: 294px; left: 0; right: 0;
    text-align: center;
    font-family: "Crimson Pro", Georgia, serif;
    font-weight: 600; font-size: 26px;
    color: var(--brand-blue);
  }
  .back__body {
    position: absolute; top: 332px; left: 0; right: 0;
    text-align: center;
    color: var(--ink);
    font-size: 14.5px; line-height: 19px;
  }
  .back__body p { margin-bottom: 8px; }
  .back__cta { font-weight: 500; }
  .back__cta .accent { color: var(--brand-blue); font-weight: 400; }
  .back__languages {
    position: absolute; top: 601px; left: 45px;
    font-size: 14.5px; line-height: 24px;
    color: var(--ink);
  }
  .back__tagline {
    position: absolute; top: 684px; left: 0; right: 0;
    text-align: center;
    color: var(--paper);
    font-weight: 600; font-size: 18px; line-height: 23px;
  }
</style>
</head>
<body>

<section class="card card--front">
  <svg class="card__shapes" width="508" height="762" viewBox="0 0 508 762">
    <defs>
      <linearGradient id="party-tones" x1="0" y1="0" x2="1" y2="1">
        <stop offset="0" stop-color="var(--photo-party-a)"/>
        <stop offset="0.5" stop-color="var(--photo-party-b)"/>
        <stop offset="1" stop-color="var(--photo-party-a)"/>
      </linearGradient>
    </defs>
    <path role="img" aria-label="Photo of a group of smiling women in festive dress raising glasses together at a party"
          d="M0,212 C120,120 350,85 508,95 L508,530 C420,620 200,640 0,600 Z"
          fill="url(#party-tones)"/>
  </svg>
  <h1 class="front__title">Mireva Party Planning...</h1>
  <div class="front__footer">
    <div>Where Great Memories Are Waiting</div>
    <div>Call Nico at <strong>(917) 555 0186</strong> or visit</div>
    <div class="front__url">www.mirevapartyplanning.com</div>
  </div>
</section>

<section class="card card--back">
  <svg class="card__shapes" width="508" height="762" viewBox="0 0 508 762">
    <defs>
      <linearGradient id="food-tones" x1="0" y1="0" x2="1" y2="1">
        <stop offset="0" stop-color="var(--photo-food-a)"/>
        <stop offset="0.6" stop-color="var(--photo-food-b)"/>
        <stop offset="1" stop-color="var(--photo-food-a)"/>
      </linearGradient>
    </defs>
    <rect role="img" aria-label="Photo of guests serving themselves from a colourful catered buffet"
          x="0" y="0" width="508" height="259" fill="url(#food-tones)"/>
    <path d="M0,690 C150,660 350,672 508,620 L508,762 L0,762 Z" fill="var(--brand-blue)"/>
  </svg>
  <h2 class="back__title">Mireva Party Planning</h2>
  <div class="back__body">
    <p>is your only choice for complete party<br>and entertainment services</p>
    <p>Weddings, Birthdays, Anniversaries, Sweet 16s,<br>
       Quinceneras, Corporate events or any event of any kind.<br>
       We are ready to help you put together an unforgettable<br>
       experience for everyone to remember</p>
    <p>We are affiliated with the best<br>
       catering halls &amp; restaurants, photo/video, international<br>
       DJs/bands, limos, wedding gowns &amp; bridesmaids dresses,<br>
       tuxedos, flowers, and specialized entertainers</p>
    <p class="back__cta">Call us today at <span class="accent">(917) 555 0186</span> or<br>
       log on to <span class="accent">www.mirevapartyplanning.com</span></p>
  </div>
  <div class="back__languages">
    <div>Hablamos Espanol</div>
    <div>Milame Ellinika</div>
  </div>
  <div class="back__tagline">Let us make your special event<br>one that will last a lifetime!</div>
</section>

</body>
</html>
```